Skin Care business card for esthetician that is home based

I need a business card for my esthetician business. I would like to use a picture provided.
I want the picture #1 that I have provided to be as the main background with my title and the moto underneath in smaller lettering. Below that as a seperate thing I would like my full name and underneath in small letters to say "esthetician".
As a seperate paragraph I would like my address then phone number, email and my website that I have provided in the business card details.
On the back side I would like my second picture to be small and in the top left corner and then have the "nice to haves" details to be at the center bottom of the card.
Target Market(s)
mosty women between 18 and 60 years old
Industry/Entity Type
Skin Care
Contact Information for Business Card
Coastline Skin Care - Main Title
Helping you find beautiful! - motto
Lorena Bistrica Vondel -
Phone: 312.485.1937
7183 SW 9th Avenue
Dallow WA 98321
marlowskincare@examplemail.com
www.marlowskincare.example
Font styles to use
Requirements
Must have
- Picure I provided or other similar photo.
Nice to have
- On the back side:
Helping you find beautiful!
www.marlowskincare.example

```html
<!DOCTYPE html>
<html lang="en">
<head>
<meta charset="utf-8">
<title>Coastline Skin Care – Business Card</title>
<link rel="stylesheet" href="https://fonts.googleapis.com/css2?family=Pinyon+Script&family=Tinos&display=swap">
<style>
  :root {
    --backdrop: #e8e5e1;
    --card: #ffffff;
    --ink: #111111;
    --title-ink: #333333;
    --pink: #d455a8;
    --photo-light: #ecd2c4;
    --photo-mid: #c99a80;
    --photo-dark: #6e4a3a;
  }
  * { box-sizing: border-box; margin: 0; padding: 0; }
  html, body {
    width: 900px; height: 1200px; overflow: hidden;
    background: var(--backdrop);
  }
  .canvas { position: relative; width: 900px; height: 1200px; }

  .card {
    position: absolute; left: 82px; width: 736px; height: 432px;
    background: var(--card); border-radius: 30px; overflow: hidden;
    box-shadow: 0 4px 14px rgba(0,0,0,0.18);
    font-family: "Tinos", "Times New Roman", serif;
  }
  .card--front { top: 128px; }
  .card--back { top: 632px; height: 430px; }

  .front-art { position: absolute; inset: 0; width: 736px; height: 432px; }

  .front-details {
    position: absolute; left: 388px; width: 300px; top: 0;
    text-align: center;
  }
  .brand-name {
    position: absolute; top: 92px; left: -30px; width: 360px;
    font-family: "Tinos", "Times New Roman", serif; font-weight: 400;
    font-size: 31px; color: var(--title-ink); white-space: nowrap;
  }
  .motto {
    position: absolute; top: 134px; width: 100%;
    font-size: 16px; color: var(--pink);
  }
  .divider-dots {
    position: absolute; width: 100%; height: 8px;
    display: flex; justify-content: center; gap: 4px;
  }
  .divider-dots span {
    width: 5px; height: 5px; border-radius: 50%; background: var(--pink);
  }
  .divider-dots--upper { top: 166px; }
  .divider-dots--lower { top: 241px; }
  .owner-name {
    position: absolute; top: 182px; width: 100%;
    font-size: 20px; color: var(--ink); font-weight: 400;
  }
  .owner-role {
    position: absolute; top: 210px; width: 100%;
    font-size: 16px; color: var(--pink);
  }
  .contact-list {
    position: absolute; top: 256px; width: 100%;
    list-style: none; font-size: 15.5px; color: var(--ink); line-height: 24px;
  }
  .contact-list li { white-space: nowrap; }

  .portrait {
    position: absolute; left: 40px; top: 32px; width: 134px; height: 134px;
    border-radius: 50%; border: 3px solid var(--pink); overflow: hidden;
  }
  .portrait svg { display: block; width: 100%; height: 100%; }

  .back-motto {
    position: absolute; left: 0; right: 0; top: 304px; text-align: center;
    font-family: "Pinyon Script", cursive; font-size: 46px; color: var(--pink);
  }
  .back-web {
    position: absolute; left: 0; right: 0; top: 374px; text-align: center;
    font-size: 15px; color: var(--pink);
  }
</style>
</head>
<body>
<main class="canvas">

  <section class="card card--front">
    <svg class="front-art" viewBox="0 0 736 432">
      <defs>
        <linearGradient id="spa-photo-tone" x1="0" y1="0" x2="0.6" y2="1">
          <stop offset="0" stop-color="#ecd2c4"/>
          <stop offset="0.55" stop-color="#c99a80"/>
          <stop offset="1" stop-color="#6e4a3a"/>
        </linearGradient>
      </defs>
      <path class="spa-photo" d="M0,0 L400,0 C310,100 290,300 420,432 L0,432 Z" fill="url(#spa-photo-tone)"
            role="img" aria-label="Photo of a woman relaxing with a facial mask during a skin care treatment"/>
    </svg>

    <div class="front-details">
      <h1 class="brand-name">Coastline Skin Care</h1>
      <p class="motto">Helping you find beautiful!</p>
      <div class="divider-dots divider-dots--upper"><span></span><span></span><span></span></div>
      <h2 class="owner-name">Lorena Bistrica Vondel</h2>
      <p class="owner-role">Esthetician</p>
      <div class="divider-dots divider-dots--lower"><span></span><span></span><span></span></div>
      <ul class="contact-list">
        <li>312.485.1937</li>
        <li>7183 SW 9th Avenue, Dallow WA 98321</li>
        <li>marlowskincare@examplemail.com</li>
        <li>www.marlowskincare.example</li>
      </ul>
    </div>
  </section>

  <section class="card card--back">
    <div class="portrait">
      <svg viewBox="0 0 100 100" role="img" aria-label="Portrait photo of the esthetician">
        <defs>
          <linearGradient id="portrait-tone" x1="0" y1="0" x2="0" y2="1">
            <stop offset="0" stop-color="#b59a7c"/>
            <stop offset="1" stop-color="#ddd6cf"/>
          </linearGradient>
        </defs>
        <rect width="100" height="100" fill="url(#portrait-tone)"/>
      </svg>
    </div>
    <p class="back-motto">Helping you find beautiful!</p>
    <p class="back-web">www.marlowskincare.example</p>
  </section>

</main>
</body>
</html>
```